Event Space Website (clone)

the name of the company is TOLVAPARTY.com
i’ll have a logo shortly

i basically need a clone of the following website
https://trovehallsnx.com/
i would really like the design to be with stock photos
and then after choosing the winner i will supply my photos
(im doing some all new photo shoots this week)

id love the designer to put their OWN spin on this site

Target Market(s)

nyc urban market

Industry/Entity Type

Event Planning

Coding

Coded - Design and coding required

Number of Pages Required

1 page

Font styles to use
Serif

Requirements
Must have
• from top to bottom ill just list what i need copied

LOCATIONS FAQ CONTACT AND SOCIAL MEDIA LINKS NEED

i need the slider ... for sure

please change classics to current locations
please show
Harlem
Brooklyn
Bronx (for bronx show an image of coming soon)

please change events with a view to
Harlem Venues
1. Tolva Northgate
2. Tolva East Northgate

please change Our biggest and boldest to Brooklyn Venues
1. Tolva Riverbend
2. Tolva Kingsfield (1)
3. Tolva kingsfield (2)
4. Tolva Kingsfield rooftop

remove latest ventures
remove asian couple kissing

keep interested in this location
keep why chose us

keep contact us area
keep social media plug in
Nice to have
• ur own flair and style

PLEASE dont forget that all the individual sections
example
tolva northgate
tolva east northgate
will have their own individual micro pages .... that will be placed under brooklyn venues (ive attached an example for clarity)

```html
<!DOCTYPE html>
<html lang="en">
<head>
<meta charset="utf-8">
<title>Tolva Party – Event Spaces</title>
<link href="https://fonts.googleapis.com/css2?family=Lora:wght@400;700&family=Lato:wght@400;700&display=swap" rel="stylesheet">
<style>
:root{
  --ink:#0f0f0f;
  --charcoal:#151515;
  --ring:#262626;
  --paper:#ffffff;
  --mist:#e9e9e9;
  --line:#8a8a8a;
  --muted:#9a9a9a;
  --hero-top:#2b1a33;
  --hero-mid:#4b2d4e;
  --hero-low:#2e1f3c;
  --serif:'Lora', Georgia, serif;
  --sans:'Lato', Arial, sans-serif;
}
*{box-sizing:border-box;margin:0;padding:0}
html,body{width:1200px;height:4472px;overflow:hidden;background:var(--ink)}
body{position:relative;font-family:var(--serif);color:var(--ink)}
section,footer{position:absolute;left:0;width:1200px;overflow:hidden}
.abs{position:absolute}
.photo{position:absolute}

/* Hero */
.hero{top:0;height:637px;background:var(--hero-top)}
.hero-photo{inset:0;background:radial-gradient(ellipse at 65% 55%,#6a4664 0%,var(--hero-mid) 35%,var(--hero-low) 70%,#1c1222 100%)}
.brand{position:absolute;left:156px;top:30px;width:170px;text-align:center;color:var(--paper);font-family:var(--serif)}
.brand-name{font-size:24px;letter-spacing:3px}
.brand-sub{font-size:11px;letter-spacing:2px;margin-top:6px}
.main-nav{position:absolute;right:180px;top:22px;display:flex;gap:42px;color:var(--paper);font-size:15px}
.hero-lead{left:156px;top:246px;color:var(--paper);font-size:42px;line-height:1;text-transform:uppercase}
.hero-big{left:154px;top:280px;color:var(--paper);font-size:118px;font-weight:700;line-height:1}
.hero-sub{left:156px;top:405px;color:var(--paper);font-size:70px;line-height:1}
.slides{left:156px;top:576px;display:flex;gap:42px}
.slide{width:188px;border-bottom:1px solid rgba(255,255,255,.25);height:28px;position:relative;color:rgba(255,255,255,.35);font-size:10px}
.slide.active{border-color:var(--paper);color:var(--paper)}
.slide .num{position:absolute;left:0;bottom:-12px;font-size:10px}
.slide .label{position:absolute;left:22px;top:4px;font-size:14px;letter-spacing:2px}

/* Section titles */
.section-title{position:absolute;left:0;width:1200px;text-align:center;font-size:45px;font-weight:400}

/* Current locations */
.locations{top:637px;height:518px;background:var(--paper)}
.loc-card{position:absolute;top:120px;width:285px;height:313px;background:var(--ink);border-bottom-right-radius:110px}
.loc-card .photo{left:19px;top:25px;width:243px;height:153px}
.loc-card .name{position:absolute;left:22px;top:206px;color:var(--paper);font-size:24px}
.soon{display:flex;align-items:center;justify-content:center;color:var(--paper);font-weight:700;font-size:21px}

/* Harlem venues */
.harlem{top:1155px;height:683px;background:var(--ink)}
.harlem .section-title{color:var(--paper);top:74px}
.ring{position:absolute;border-radius:50%;border:58px solid var(--ring)}
.venue-wide{position:absolute;top:167px;width:434px;height:389px;border-top-right-radius:90px;border-bottom-right-radius:90px}
.venue-frame{position:absolute;border:2px solid rgba(255,255,255,.8);border-left-width:2px;border-top-right-radius:75px;border-bottom-right-radius:75px}
.venue-wide-name{position:absolute;top:573px;color:var(--paper);font-size:24px;text-transform:uppercase}

/* Brooklyn venues */
.brooklyn{top:1838px;height:556px;background:var(--paper)}
.venue-tile{position:absolute;top:128px;width:208px}
.venue-tile .photo{position:relative;width:208px;height:183px}
.venue-tile .name{position:relative;margin-top:36px;font-size:24px;line-height:30px;text-transform:uppercase}
.dash{position:absolute;top:207px;left:69px;width:139px;height:139px;border-radius:50%;border:1px dashed var(--line)}

/* Interested */
.interest{top:2394px;height:564px;background:linear-gradient(180deg,#f3f3f3 0%,#c8c8c8 30%,#5a5a5a 68%,#161616 100%)}
.interest .section-title{top:92px;color:var(--ink)}
.step{position:absolute;top:184px;width:200px;text-align:center}
.step-arch{position:relative;margin:0 auto;width:186px;height:200px;background:var(--ink);border-radius:93px 93px 0 0}
.step-arch svg{position:absolute;left:-14px;top:48px}
.step-num{position:absolute;left:0;right:0;top:68px;font-size:44px;color:var(--ink)}
.step-label{margin-top:40px;color:var(--paper);font-size:22px;line-height:28px;text-transform:uppercase}

/* Why choose us */
.why{top:2958px;height:533px;background:var(--ink)}
.why .section-title{color:var(--paper);top:126px}
.why-item{position:absolute;top:226px;width:220px;text-align:center;color:var(--paper)}
.why-item svg{display:block;margin:0 auto}
.why-item .label{margin-top:12px;font-size:22px;text-transform:uppercase}

/* Contact */
.contact{top:3491px;height:487px;background:var(--charcoal)}
.contact-form{position:absolute;left:0;top:0;width:667px;height:487px;background:var(--paper)}
.contact-form h2{position:absolute;left:156px;top:62px;font-size:44px;font-weight:400}
.field{position:absolute;border-bottom:1px solid var(--line);font-family:var(--sans);font-size:14px;height:22px;color:#333}
.field.select::after{content:"";position:absolute;right:4px;top:3px;width:7px;height:7px;border-right:1px solid #555;border-bottom:1px solid #555;transform:rotate(45deg)}
.submit{position:absolute;left:156px;top:389px;width:126px;height:34px;border-radius:17px;background:var(--ink);color:var(--paper);font-family:var(--sans);font-size:15px;line-height:34px;padding-left:20px}
.submit i{position:absolute;right:4px;top:4px;width:26px;height:26px;border-radius:50%;background:var(--paper)}
.info-panel{position:absolute;left:667px;top:0;width:533px;height:487px;background:radial-gradient(ellipse at 40% 40%,#2c2c2c 0%,#161616 60%,#0b0b0b 100%)}
.info-panel h2{position:absolute;left:43px;top:76px;color:var(--paper);font-size:42px;font-weight:400}
.info-row{position:absolute;left:43px;color:var(--paper);font-family:var(--sans);font-size:15px;display:flex;gap:26px}
.info-row svg{flex:none;margin-top:1px}

/* Footer */
.site-footer{top:3978px;height:494px;background:#0c0c0c;color:var(--paper)}
.foot-brand{position:absolute;left:156px;top:110px;font-size:20px;letter-spacing:3px}
.foot-brand small{display:block;font-size:10px;letter-spacing:2px;margin-top:4px}
.foot-text{position:absolute;left:156px;top:211px;width:290px;font-family:var(--sans);font-size:15px;line-height:22px}
.newsletter{position:absolute;left:156px;top:293px;width:282px;height:32px;border-radius:16px;background:var(--paper);font-family:var(--sans);font-size:13px;color:#333;line-height:32px;padding-left:24px}
.newsletter b{position:absolute;right:0;top:0;width:132px;height:32px;border-radius:16px;background:#1d1d1d;color:var(--paper);font-weight:400;padding-left:20px;font-size:15px}
.newsletter b i{position:absolute;right:3px;top:3px;width:26px;height:26px;border-radius:50%;background:var(--paper)}
.foot-head{position:absolute;top:124px;font-size:20px}
.social-grid{position:absolute;left:497px;top:185px;display:grid;grid-template-columns:repeat(4,69px);grid-auto-rows:64px;gap:6px}
.social-grid div{position:relative}
.handle{position:absolute;left:100px;top:8px;width:120px;height:46px;background:#1fa3d8;color:var(--paper);font-family:var(--sans);font-size:13px;text-align:center;line-height:46px;z-index:2}
.foot-list{position:absolute;left:863px;top:183px;list-style:none;font-family:var(--sans);font-size:15px}
.foot-list li{height:33px;position:relative;padding-left:29px}
.foot-list li::before{content:"";position:absolute;left:4px;top:7px;width:5px;height:5px;border-radius:50%;background:var(--paper)}
.foot-rule{position:absolute;left:156px;top:391px;width:888px;border-top:1px solid #2a2a2a}
.to-top{position:absolute;left:993px;top:374px;width:34px;height:34px;border-radius:50%;background:#141414}
.copyright{position:absolute;left:156px;top:422px;font-family:var(--sans);font-size:14px;color:#3a3a3a}
.copyright b{color:var(--paper);font-weight:400;margin:0 10px}
</style>
</head>
<body>

<section class="hero">
  <div class="photo hero-photo" role="img" aria-label="Banquet hall set with round tables, chairs and soft violet lighting"></div>
  <div class="brand"><div class="brand-name">TOLVA PARTY</div><div class="brand-sub">BROOKLYN HARLEM</div></div>
  <nav class="main-nav"><span>Location</span><span>FAQ</span><span>Contact</span></nav>
  <p class="abs hero-lead">We are perfect</p>
  <h1 class="abs hero-big">For Large</h1>
  <p class="abs hero-sub">Scale Events</p>
  <div class="abs slides">
    <div class="slide active"><span class="num">1.</span><span class="label">WEDDING EVENT</span></div>
    <div class="slide"><span class="num">2.</span></div>
    <div class="slide"><span class="num">3.</span></div>
    <div class="slide"><span class="num">4.</span></div>
  </div>
</section>

<section class="locations">
  <h2 class="section-title" style="top:46px">Current Locations</h2>
  <article class="loc-card" style="left:158px">
    <div class="photo" role="img" aria-label="Windmill by the water at night with lights" style="background:linear-gradient(180deg,#1d3a8a 0%,#2d4fa8 55%,#c98a2c 80%,#2a1d10 100%)"></div>
    <h3 class="name">HARLEM</h3>
  </article>
  <article class="loc-card" style="left:459px">
    <div class="photo" role="img" aria-label="Bridge and city skyline at dusk" style="background:linear-gradient(180deg,#5a6e98 0%,#3a4a70 50%,#1d2230 100%)"></div>
    <h3 class="name">BROOKLYN</h3>
  </article>
  <article class="loc-card" style="left:759px">
    <div class="photo soon" role="img" aria-label="Dim event room, coming soon" style="background:linear-gradient(180deg,#4a4f63 0%,#2b2f40 100%)">COMING SOON</div>
    <h3 class="name">BRONX</h3>
  </article>
</section>

<section class="harlem">
  <div class="ring" style="left:-110px;top:370px;width:270px;height:270px"></div>
  <div class="ring" style="left:955px;top:0;width:330px;height:330px"></div>
  <h2 class="section-title">Harlem Venues</h2>
  <div class="venue-wide" role="img" aria-label="Couple at an evening party under string lights" style="left:158px;background:radial-gradient(ellipse at 45% 30%,#c88a4a 0%,#6b3f22 40%,#1e120b 100%)"></div>
  <div class="venue-frame" style="left:186px;top:191px;width:379px;height:339px"></div>
  <div class="venue-wide" role="img" aria-label="Audience at a talk in a blue-lit hall" style="left:608px;background:linear-gradient(135deg,#4e5fe0 0%,#3a46c8 45%,#1d2288 100%)"></div>
  <div class="venue-frame" style="left:636px;top:191px;width:379px;height:339px"></div>
  <h3 class="venue-wide-name" style="left:158px">Tolva Northgate</h3>
  <h3 class="venue-wide-name" style="left:608px">Tolva East Northgate</h3>
</section>

<section class="brooklyn">
  <h2 class="section-title" style="top:50px">Brooklyn Venues</h2>
  <article class="venue-tile" style="left:158px">
    <div class="photo" role="img" aria-label="Seated audience facing a lit stage" style="background:linear-gradient(180deg,#0c1020 0%,#27355a 60%,#0a0d18 100%)"></div>
    <div class="dash"></div>
    <h3 class="name">Tolva<br>Riverbend</h3>
  </article>
  <article class="venue-tile" style="left:384px">
    <div class="photo" role="img" aria-label="Guests mingling at a candlelit reception" style="background:linear-gradient(180deg,#b9a98f 0%,#6a5038 60%,#2a1c12 100%)"></div>
    <div class="dash"></div>
    <h3 class="name">Tolva<br>Kingsfield</h3>
  </article>
  <article class="venue-tile" style="left:610px">
    <div class="photo" role="img" aria-label="Table with flowers and glassware" style="background:linear-gradient(180deg,#3d5a7a 0%,#c8905a 50%,#e8e0d2 100%)"></div>
    <div class="dash"></div>
    <h3 class="name">Tolva<br>Kingsfield</h3>
  </article>
  <article class="venue-tile" style="left:834px">
    <div class="photo" role="img" aria-label="Ballroom with round tables and chandeliers" style="background:linear-gradient(180deg,#d9c6ad 0%,#b49a7a 55%,#8a7560 100%)"></div>
    <div class="dash"></div>
    <h3 class="name">Tolva<br>Kingsfield<br>Rooftop</h3>
  </article>
</section>

<section class="interest">
  <svg class="abs" style="left:0;top:90px" width="70" height="420" viewBox="0 0 70 420"><path d="M0 0 C40 10 60 60 45 120 C30 180 70 230 55 300 C45 360 20 400 0 420 Z" fill="#efefef"/></svg>
  <svg class="abs" style="right:0;top:30px" width="50" height="380" viewBox="0 0 50 380"><path d="M50 0 C20 40 30 120 40 180 C48 240 20 320 50 380 Z" fill="#efefef"/></svg>
  <h2 class="section-title">Interested In This Location ?</h2>
  <div class="step" style="left:162px">
    <div class="step-arch"><svg width="214" height="110" viewBox="0 0 214 110"><path d="M10 50 C6 20 40 8 90 10 C140 4 200 12 206 40 C214 55 198 70 204 82 C190 104 120 100 80 104 C40 106 4 96 12 78 C0 70 14 60 10 50 Z" fill="#fff"/></svg><span class="step-num">01</span></div>
    <p class="step-label">Send us a<br>note</p>
  </div>
  <div class="step" style="left:388px">
    <div class="step-arch"><svg width="214" height="110" viewBox="0 0 214 110"><path d="M10 50 C6 20 40 8 90 10 C140 4 200 12 206 40 C214 55 198 70 204 82 C190 104 120 100 80 104 C40 106 4 96 12 78 C0 70 14 60 10 50 Z" fill="#fff"/></svg><span class="step-num">02</span></div>
    <p class="step-label">Check out<br>the location</p>
  </div>
  <div class="step" style="left:614px">
    <div class="step-arch"><svg width="214" height="110" viewBox="0 0 214 110"><path d="M10 50 C6 20 40 8 90 10 C140 4 200 12 206 40 C214 55 198 70 204 82 C190 104 120 100 80 104 C40 106 4 96 12 78 C0 70 14 60 10 50 Z" fill="#fff"/></svg><span class="step-num">03</span></div>
    <p class="step-label">Pick your<br>perfect date</p>
  </div>
  <div class="step" style="left:838px">
    <div class="step-arch"><svg width="214" height="110" viewBox="0 0 214 110"><path d="M10 50 C6 20 40 8 90 10 C140 4 200 12 206 40 C214 55 198 70 204 82 C190 104 120 100 80 104 C40 106 4 96 12 78 C0 70 14 60 10 50 Z" fill="#fff"/></svg><span class="step-num">04</span></div>
    <p class="step-label">Send us a<br>note</p>
  </div>
</section>

<section class="why">
  <h2 class="section-title">Why Choose Us</h2>
  <div class="why-item" style="left:151px">
    <svg width="136" height="136" viewBox="0 0 136 136"><circle cx="68" cy="68" r="64" fill="none" stroke="#fff" stroke-width="3"/><path d="M44 70 L60 86 L92 52" fill="none" stroke="#fff" stroke-width="7" stroke-linecap="round" stroke-linejoin="round"/></svg>
    <p class="label" style="text-transform:none">Easy</p>
  </div>
  <div class="why-item" style="left:377px">
    <svg width="136" height="136" viewBox="0 0 136 136"><circle cx="68" cy="68" r="64" fill="none" stroke="#fff" stroke-width="3"/><rect x="44" y="46" width="44" height="32" rx="4" fill="#fff"/><path d="M52 78 L52 90 L64 78 Z" fill="#fff"/><path d="M92 58 H96 V88 L88 82 H64" fill="none" stroke="#fff" stroke-width="4"/><path d="M51 56 H80 M51 64 H80 M51 71 H70" stroke="#0f0f0f" stroke-width="3"/></svg>
    <p class="label">Responsive</p>
  </div>
  <div class="why-item" style="left:602px">
    <svg width="136" height="136" viewBox="0 0 136 136"><circle cx="68" cy="68" r="64" fill="none" stroke="#fff" stroke-width="3"/><rect x="44" y="46" width="48" height="42" rx="3" fill="none" stroke="#fff" stroke-width="3"/><path d="M44 54 H92" stroke="#fff" stroke-width="3"/><circle cx="68" cy="72" r="9" fill="none" stroke="#fff" stroke-width="3"/><circle cx="68" cy="72" r="3" fill="#fff"/></svg>
    <p class="label">Customizable</p>
  </div>
  <div class="why-item" style="left:828px">
    <svg width="136" height="136" viewBox="0 0 136 136"><circle cx="68" cy="68" r="64" fill="none" stroke="#fff" stroke-width="3"/><path d="M54 62 V52 A14 14 0 0 1 82 52 V62" fill="none" stroke="#fff" stroke-width="4"/><rect x="48" y="62" width="40" height="32" rx="4" fill="none" stroke="#fff" stroke-width="4"/><circle cx="68" cy="76" r="4" fill="#fff"/><path d="M68 78 V86" stroke="#fff" stroke-width="3"/></svg>
    <p class="label">Vendors</p>
  </div>
</section>

<section class="contact">
  <form class="contact-form">
    <h2>Send Us A Message</h2>
    <div class="field" style="left:156px;top:144px;width:217px">Name :</div>
    <div class="field" style="left:389px;top:144px;width:217px">Email :</div>
    <div class="field" style="left:156px;top:197px;width:217px">Phone :</div>
    <div class="field select" style="left:389px;top:197px;width:217px">Type Of Event :</div>
    <div class="field select" style="left:156px;top:252px;width:450px">Venue Of Interest :</div>
    <div class="field" style="left:156px;top:327px;width:450px">Message :</div>
    <div class="submit">Submit<i></i></div>
  </form>
  <div class="info-panel" role="img" aria-label="Dark crowd at a party">
    <h2>Info</h2>
    <div class="info-row" style="top:157px"><svg width="14" height="14" viewBox="0 0 24 24"><path d="M5 2 L9 2 L11 7 L8 9 C9 12 12 15 15 16 L17 13 L22 15 L22 19 C22 21 20 22 18 22 C9 21 3 15 2 6 C2 4 3 2 5 2 Z" fill="#fff"/></svg><span>Phone : 123-456-789</span></div>
    <div class="info-row" style="top:199px"><svg width="14" height="14" viewBox="0 0 24 24"><rect x="2" y="5" width="20" height="14" fill="#fff"/><path d="M2 5 L12 13 L22 5" fill="none" stroke="#161616" stroke-width="2"/></svg><span>Mail :&nbsp;&nbsp; hello@tolvaparty.com</span></div>
    <div class="info-row" style="top:240px"><svg width="14" height="16" viewBox="0 0 24 28"><path d="M12 0 C5 0 1 5 1 11 C1 18 12 28 12 28 C12 28 23 18 23 11 C23 5 19 0 12 0 Z" fill="#fff"/><circle cx="12" cy="11" r="4" fill="#161616"/></svg><span>Address : Loremipsumdoallr,<br>&nbsp;&nbsp;&nbsp;&nbsp;&nbsp;&nbsp;&nbsp;&nbsp;&nbsp;&nbsp;&nbsp;&nbsp;&nbsp;&nbsp;Harlem</span></div>
  </div>
</section>

<footer class="site-footer">
  <div class="foot-brand">TOLVA PARTY<small>BROOKLYN HARLEM</small></div>
  <p class="foot-text">Many desktop publishing packages and web page editors now use Lorem Ipsum as their default model text .</p>
  <div class="newsletter">Enter Mail ID<b>Subscribe<i></i></b></div>

  <h4 class="foot-head" style="left:497px;font-weight:400">Lets Get Social</h4>
  <div class="social-grid">
    <div role="img" aria-label="Blue-lit audience" style="background:#3a46c8"></div>
    <div role="img" aria-label="Party lights" style="background:#6b3f22"></div>
    <div role="img" aria-label="Venue interior" style="background:#3a4a70"></div>
    <div role="img" aria-label="Reception guests" style="background:#5a2e24"></div>
    <div role="img" aria-label="Windmill at night" style="background:#2d4fa8"></div>
    <div role="img" aria-label="City skyline" style="background:#3a4a70"></div>
    <div role="img" aria-label="Event room" style="background:#2b2f40"></div>
    <div role="img" aria-label="Dinner table" style="background:#b49a7a"></div>
    <span class="handle">@tolvaparty</span>
  </div>

  <h4 class="foot-head" style="left:863px;font-weight:400">Harlem Venues</h4>
  <ul class="foot-list">
    <li>Long established fact</li>
    <li>Contrary to popular</li>
    <li>Long established fact</li>
    <li>Contrary to popular</li>
    <li>Long established fact</li>
  </ul>

  <div class="foot-rule"></div>
  <div class="to-top"><svg width="34" height="34" viewBox="0 0 34 34"><path d="M17 24 V10 M12 15 L17 10 L22 15" fill="none" stroke="#fff" stroke-width="1.5"/></svg></div>
  <p class="copyright">Copyright©2021<b>Tolvaparty</b>All Rights Reserved</p>
</footer>

</body>
</html>
```